Hi,

I have just started up a business called VELUMO in Melbourne. We run fun street art tours around Melbourne's CBD.

I need to create a design for the back side of my business cards. I have designed the front side (simply with my logo) however, I am having trouble designing the reverse side in a professional manner. I have attached pictures of what I have done.

The picture attached titled "VELUMO Business Cards Back" has all the information that I require on the back side of my business cards; although displayed in an amateur and simple way. As displayed in the picture, I need: the VELUMO logo, the website URL, the booking details (phone - 0481 556 217 & email - bookings@velumo.com.au) and the service description ($20, One Hour, Tours Daily, Meet at Carrow Rd Terminal). I would also like to use the font in the picture supplied which is "source-sans-pro".

The VELUMO tours are for tourists and are relaxed, entertaining and fun! I would like the design to reflect this.

Target Market(s)

Backpackers & University Students

Industry/Entity Type

Business

Requirements
Must have
• The VELUMO logo, the website URL, the booking details (phone - 0481 556 217 & email - bookings@velumo.com.au) and the service description ($20, One Hour, Tours Daily, Meet at Carrow Rd Terminal).

```html
<!DOCTYPE html>
<html lang="en">
<head>
<meta charset="utf-8">
<title>VELUMO Business Card Back</title>
<link rel="stylesheet" href="https://fonts.googleapis.com/css2?family=Josefin+Sans:wght@400;600;700&display=swap">
<style>
  :root {
    --paper: #ffffff;
    --tile-red: #f84842;
    --ink: #111111;
    --light: #ffffff;
  }
  html, body {
    margin: 0;
    padding: 0;
    width: 1200px;
    height: 777px;
    overflow: hidden;
    background: var(--paper);
  }
  .card {
    position: relative;
    width: 1200px;
    height: 777px;
    background: var(--paper);
    font-family: "Josefin Sans", sans-serif;
    color: var(--light);
  }
  .brand-name {
    position: absolute;
    left: 0;
    width: 1200px;
    top: 104px;
    margin: 0;
    text-align: center;
    font-weight: 700;
    font-size: 124px;
    line-height: 1;
    letter-spacing: 6px;
    color: var(--ink);
  }
  .website {
    position: absolute;
    left: 0;
    width: 1200px;
    top: 276px;
    text-align: center;
    font-weight: 600;
    font-size: 35px;
    line-height: 1;
    color: var(--tile-red);
  }
  .tile, .bar {
    position: absolute;
    background: var(--tile-red);
    display: flex;
    align-items: center;
    justify-content: center;
    text-align: center;
    font-variant: small-caps;
    font-weight: 600;
    line-height: 1;
  }
  .tile {
    top: 338px;
    height: 150px;
    width: 272px;
    font-size: 54px;
  }
  .tile--price { left: 24px; font-size: 62px; font-variant: normal; font-weight: 700; }
  .tile--schedule { left: 314px; width: 273px; }
  .tile--duration { left: 610px; }
  .tile--meeting { left: 904px; width: 271px; font-size: 50px; }
  .bar {
    left: 24px;
    width: 1151px;
    height: 68px;
  }
  .bar--call { top: 506px; font-size: 53px; }
  .bar--phone { top: 590px; font-variant: normal; font-size: 62px; letter-spacing: 2px; }
  .bar--email { top: 676px; font-size: 50px; }
  .bar span, .tile span { display: block; padding-top: 8px; }
</style>
</head>
<body>
  <main class="card">
    <h1 class="brand-name">VELUMO</h1>
    <div class="website">www.velumo.com.au</div>

    <div class="tile tile--price"><span>$20</span></div>
    <div class="tile tile--schedule"><span>Daily<br>Tours</span></div>
    <div class="tile tile--duration"><span>One<br>Hour</span></div>
    <div class="tile tile--meeting"><span>Carrow Rd<br>Terminal</span></div>

    <div class="bar bar--call"><span>Call JAX to Book Now</span></div>
    <div class="bar bar--phone"><span>0481 556 217</span></div>
    <div class="bar bar--email"><span>bookings@velumo.com.au</span></div>
  </main>
</body>
</html>
```